Heritage Hollow Business Cards

Require a business card design. <br/><br/>Needs to include logo (either round or long version) plus these details:<br/>Maya Torvel<br/>Heritage Hollow<br/>maya@quonbrook.com.au<br/>02 6481 7390<br/>PO Box Glenwarra NSW 2913<br/>www.heritagehollow.com.au<br/><br/>I need in an editable format so that I can create for multiple staff members. <br/><br/>

Target Market(s)

We are an online store selling renovation products to home owners are builders. Looking for a classic classy design.

Industry/Entity Type

Home And Garden

Contact Information for Business Card

Maya Torvel
Heritage Hollow
maya@quonbrook.com.au
02 6481 7390
PO Box Glenwarra NSW 2913
www.heritagehollow.com.au

Colors

Designer to choose colors to be used in the design.

Requirements
Must have
• Must include Logo.

```html
<!DOCTYPE html>
<html lang="en">
<head>
<meta charset="UTF-8">
<title>Heritage Hollow Business Cards</title>
<link rel="stylesheet" href="https://fonts.googleapis.com/css2?family=Poppins:wght@400;500;600&display=swap">
<style>
  :root {
    --stage: #2b2b2b;
    --sage: #5b7a69;
    --sage-deep: #4d6a5a;
    --sage-line: #46685a;
    --paper: #ffffff;
    --ink: #1f1f1f;
    --ink-soft: #2e2e2e;
  }
  * { box-sizing: border-box; margin: 0; padding: 0; }
  html, body { width: 1200px; height: 900px; overflow: hidden; }
  body {
    background: var(--stage);
    font-family: "Poppins", sans-serif;
    position: relative;
  }
  .card {
    position: absolute;
    left: 250px;
    width: 700px;
    height: 400px;
  }
  .card-back {
    top: 40px;
    background: var(--sage);
    display: flex;
    align-items: center;
    justify-content: center;
  }
  .emblem {
    width: 230px;
    height: 230px;
    border: 2px solid var(--sage-deep);
    border-radius: 50%;
    display: flex;
    align-items: center;
    justify-content: center;
    text-align: center;
  }
  .emblem-name {
    color: var(--sage-deep);
    font-weight: 600;
    font-size: 34px;
    line-height: 1.1;
  }
  .card-front {
    top: 465px;
    background: var(--paper);
    color: var(--ink);
  }
  .brand {
    position: absolute;
    left: 46px;
    top: 52px;
    display: flex;
    align-items: center;
    gap: 14px;
  }
  .brand-dot {
    width: 44px;
    height: 44px;
    border: 2px solid var(--ink-soft);
    border-radius: 50%;
  }
  .brand-name {
    font-weight: 500;
    font-size: 34px;
    color: var(--ink-soft);
  }
  .rule {
    position: absolute;
    left: 50px;
    right: 50px;
    top: 215px;
    height: 2px;
    background: var(--sage-line);
  }
  .person {
    position: absolute;
    right: 50px;
    top: 158px;
    text-align: right;
    line-height: 1.2;
  }
  .person-name { color: var(--sage); font-weight: 600; font-size: 19px; }
  .person-company { font-size: 17px; }
  .contacts {
    position: absolute;
    left: 50px;
    top: 236px;
    list-style: none;
    font-size: 17px;
  }
  .contacts li {
    display: flex;
    align-items: center;
    gap: 12px;
    height: 32px;
  }
  .contacts svg { width: 20px; height: 20px; fill: var(--sage); }
  .address {
    position: absolute;
    right: 50px;
    bottom: 40px;
    text-align: right;
    font-size: 18px;
    line-height: 1.5;
  }
</style>
</head>
<body>
  <section class="card card-back" aria-label="Card back">
    <div class="emblem">
      <span class="emblem-name">Heritage<br>Hollow</span>
    </div>
  </section>

  <section class="card card-front" aria-label="Card front">
    <div class="brand">
      <span class="brand-dot"></span>
      <span class="brand-name">Heritage Hollow</span>
    </div>

    <div class="person">
      <div class="person-name">Maya Torvel</div>
      <div class="person-company">Heritage Hollow</div>
    </div>

    <div class="rule"></div>

    <ul class="contacts">
      <li>
        <svg viewBox="0 0 24 24" aria-hidden="true"><path d="M6.6 10.8a15.1 15.1 0 0 0 6.6 6.6l2.2-2.2c.3-.3.7-.4 1-.2 1.1.4 2.3.6 3.6.6.6 0 1 .4 1 1V20c0 .6-.4 1-1 1A17 17 0 0 1 3 4c0-.6.4-1 1-1h3.5c.6 0 1 .4 1 1 0 1.3.2 2.5.6 3.6.1.3 0 .7-.2 1z"/></svg>
        <span>02 6481 7390</span>
      </li>
      <li>
        <svg viewBox="0 0 24 24" aria-hidden="true"><path d="M2 5h20v2l-10 6L2 7z"/><path d="M2 9l10 6 10-6v10H2z"/></svg>
        <span>maya@quonbrook.com.au</span>
      </li>
      <li>
        <svg viewBox="0 0 24 24" aria-hidden="true"><path d="M12 2a10 10 0 1 0 0 20 10 10 0 0 0 0-20zm-1 17.9A8 8 0 0 1 4.2 10.8L9 15.5v1a2 2 0 0 0 2 2zm6.9-2.5A2 2 0 0 0 16 16h-1v-3a1 1 0 0 0-1-1H8v-2h2a1 1 0 0 0 1-1V7h2a2 2 0 0 0 2-2v-.4a8 8 0 0 1 2.9 12.8z"/></svg>
        <span>www.heritagehollow.com.au</span>
      </li>
    </ul>

    <address class="address" style="font-style: normal;">
      PO Box<br>Glenwarra NSW 2913
    </address>
  </section>
</body>
</html>
```